Commercial Piping Company Needs A Modern Business Card

We need a clean business card for our commercial pipe lining company. We would like to see a mock up in two color schemes: Black, Grey and Blue and Black, Grey and Orange. We are in the piping industry, but want a professional, clean and modern look to the card.

Industry/Entity Type

Plumbing

Contact Information for Business Card

Name: Mark Tollen
Title: Managing Partner
Phone: 382.615.9073
Email: Mark@VantoPipe.Net

Requirements
Must have
• Back Side Should Have a White Back Ground with Full Logo. Front I would like to see a couple lay outs for contact info. Also the final card will have rounded edges, so please take that into account for printing.
Nice to have
• Two Color Palette Examples
Should not have
• No need for an address line

```html
<!DOCTYPE html>
<html lang="en">
<head>
<meta charset="utf-8">
<title>VantoPipe Business Card</title>
<link rel="stylesheet" href="https://fonts.googleapis.com/css2?family=Montserrat:wght@400;500&display=swap">
<style>
  :root {
    --backdrop: #3a3a3c;
    --card-white: #ffffff;
    --card-dark: #1e1e20;
    --ink-black: #111111;
    --brand-blue: #1a9be6;
    --text-grey: #a3a3a6;
  }
  * { margin: 0; padding: 0; box-sizing: border-box; }
  html, body {
    width: 1200px;
    height: 1000px;
    overflow: hidden;
  }
  body {
    background: var(--backdrop);
    font-family: "Montserrat", Arial, sans-serif;
    position: relative;
  }
  .card {
    position: absolute;
    width: 620px;
    height: 354px;
    border-radius: 26px;
    box-shadow: 0 18px 40px rgba(0,0,0,0.45);
    overflow: hidden;
  }
  .card--back {
    left: 470px;
    top: 80px;
    background: var(--card-white);
    color: var(--ink-black);
  }
  .card--front {
    left: 110px;
    top: 520px;
    background: var(--card-dark);
    color: var(--brand-blue);
  }
  .wordmark {
    position: absolute;
    line-height: 1;
    font-weight: 500;
    white-space: nowrap;
  }
  .card--back .wordmark {
    left: 0;
    right: 0;
    top: 118px;
    text-align: center;
  }
  .card--front .wordmark {
    right: 48px;
    top: 44px;
    text-align: right;
  }
  .wordmark__name {
    font-size: 48px;
    letter-spacing: 1px;
  }
  .wordmark__tagline {
    font-size: 15px;
    letter-spacing: 1px;
    margin-top: 8px;
    line-height: 1.25;
  }
  .card--front .wordmark__name { font-size: 40px; }
  .card--front .wordmark__tagline { font-size: 13px; margin-top: 6px; }
  .contact {
    position: absolute;
    left: 0;
    top: 190px;
    padding-left: 40px;
  }
  .contact__accent {
    position: absolute;
    left: 0;
    top: 0;
    width: 12px;
    height: 34px;
    background: var(--brand-blue);
  }
  .contact__name {
    font-size: 20px;
    font-weight: 500;
    color: var(--brand-blue);
    letter-spacing: 0.4px;
  }
  .contact__title {
    font-size: 12px;
    color: var(--text-grey);
    margin-top: 1px;
  }
  .contact__list {
    list-style: none;
    margin-top: 18px;
  }
  .contact__item {
    display: flex;
    align-items: center;
    gap: 8px;
    font-size: 13px;
    color: var(--text-grey);
    margin-bottom: 4px;
  }
  .contact__icon { width: 11px; height: 11px; flex: none; }
</style>
</head>
<body>
  <section class="card card--back" aria-label="Card back">
    <div class="wordmark">
      <div class="wordmark__name">VANTOPIPE</div>
      <div class="wordmark__tagline">COMMERCIAL PIPE LINING<br>INSPECT • LINE • RENEW</div>
    </div>
  </section>

  <section class="card card--front" aria-label="Card front">
    <div class="wordmark">
      <div class="wordmark__name">VANTOPIPE</div>
      <div class="wordmark__tagline">COMMERCIAL PIPE LINING<br>INSPECT • LINE • RENEW</div>
    </div>

    <div class="contact">
      <span class="contact__accent"></span>
      <div class="contact__name">MARK TOLLEN</div>
      <div class="contact__title">Managing Partner</div>
      <ul class="contact__list">
        <li class="contact__item">
          <svg class="contact__icon" viewBox="0 0 24 24" aria-hidden="true"><path fill="#1a9be6" d="M6.6 10.8a15.1 15.1 0 0 0 6.6 6.6l2.2-2.2a1 1 0 0 1 1-.25 11.4 11.4 0 0 0 3.6.57 1 1 0 0 1 1 1V20a1 1 0 0 1-1 1A17 17 0 0 1 3 4a1 1 0 0 1 1-1h3.5a1 1 0 0 1 1 1c0 1.25.2 2.45.57 3.57a1 1 0 0 1-.25 1z"/></svg>
          382.615.9073
        </li>
        <li class="contact__item">
          <svg class="contact__icon" viewBox="0 0 24 24" aria-hidden="true"><rect x="2" y="5" width="20" height="14" rx="2" fill="#1a9be6"/><path d="M3 6l9 7 9-7" fill="none" stroke="#1e1e20" stroke-width="2"/></svg>
          Mark@VantoPipe.Net
        </li>
      </ul>
    </div>
  </section>
</body>
</html>
```